Dane Calloway Photography

Would like the Business card to have a cool logo. I’m targeting wedding/ engagement: portrait photography. My phone number on it. And my business email address.

Target Market(s)

Wedding/portrait/engagement photography.

```html
<!DOCTYPE html>
<html lang="en">
<head>
<meta charset="utf-8">
<title>Dane Calloway Photography – Business Card</title>
<link rel="stylesheet" href="https://fonts.googleapis.com/css2?family=Cormorant+Garamond:wght@500;600&display=swap">
<style>
  :root {
    --stage: #a9a8a9;
    --card: #000000;
    --ink: #ffffff;
    --gold: #c9a458;
    --serif: "Cormorant Garamond", "Times New Roman", serif;
    --sans: Arial, Helvetica, sans-serif;
  }
  html, body {
    margin: 0;
    width: 1200px;
    height: 1200px;
    overflow: hidden;
    background: var(--stage);
  }
  .stage {
    position: relative;
    width: 1200px;
    height: 1200px;
  }
  .card {
    position: absolute;
    top: 335px;
    width: 530px;
    height: 530px;
    background: var(--card);
    box-shadow: 0 18px 40px rgba(0,0,0,0.25);
    color: var(--ink);
  }
  .card--back { left: 45px; }
  .card--front { left: 625px; }

  .wordmark {
    position: absolute;
    left: 0;
    right: 0;
    text-align: center;
    font-family: var(--serif);
    font-weight: 600;
    color: var(--ink);
    line-height: 1;
  }
  .wordmark__name {
    display: block;
    font-size: 40px;
    letter-spacing: 1px;
    text-transform: uppercase;
  }
  .wordmark__trade {
    display: block;
    margin-top: 8px;
    font-size: 30px;
    letter-spacing: 2px;
  }
  .card--back .wordmark { top: 330px; }
  .card--front .wordmark { top: 230px; }

  .mark-circle {
    position: absolute;
    left: 50%;
    top: 80px;
    width: 120px;
    height: 120px;
    margin-left: -62px;
    border: 4px solid var(--ink);
    border-radius: 50%;
  }

  .corner {
    position: absolute;
    width: 48px;
    height: 48px;
    border: 0 solid var(--gold);
  }
  .corner--tl { top: 24px; left: 24px; border-top-width: 5px; border-left-width: 5px; }
  .corner--tr { top: 24px; right: 24px; border-top-width: 5px; border-right-width: 5px; }
  .corner--bl { bottom: 24px; left: 24px; border-bottom-width: 5px; border-left-width: 5px; }
  .corner--br { bottom: 24px; right: 24px; border-bottom-width: 5px; border-right-width: 5px; }

  .services {
    position: absolute;
    top: 355px;
    left: 0;
    right: 0;
    text-align: center;
    font-family: var(--serif);
    font-weight: 500;
    font-size: 23px;
    color: var(--ink);
  }
  .contacts {
    position: absolute;
    top: 405px;
    left: 40px;
    right: 40px;
    display: flex;
    justify-content: space-between;
    align-items: center;
    font-family: var(--sans);
    font-size: 17px;
    color: var(--ink);
  }
  .contact {
    display: flex;
    align-items: center;
    gap: 8px;
  }
  .contact__at {
    color: var(--gold);
    font-weight: 700;
    font-size: 24px;
  }
  .contact__phone-icon { width: 26px; height: 26px; }
</style>
</head>
<body>
<main class="stage">
  <section class="card card--back" aria-label="Card back">
    <div class="wordmark">
      <span class="wordmark__name">Dane Calloway</span>
      <span class="wordmark__trade">Photography</span>
    </div>
  </section>

  <section class="card card--front" aria-label="Card front">
    <span class="corner corner--tl"></span>
    <span class="corner corner--tr"></span>
    <span class="corner corner--bl"></span>
    <span class="corner corner--br"></span>

    <span class="mark-circle" aria-hidden="true"></span>
    <div class="wordmark">
      <span class="wordmark__name">Dane Calloway</span>
      <span class="wordmark__trade">Photography</span>
    </div>

    <p class="services">Wedding / Portrait / Engagement photography</p>

    <div class="contacts">
      <span class="contact contact--email">
        <span class="contact__at">@</span>
        hello@danecallowayphoto.com
      </span>
      <span class="contact contact--phone">
        <svg class="contact__phone-icon" viewBox="0 0 24 24" aria-hidden="true">
          <path fill="var(--gold)" d="M6.6 10.8c1.4 2.8 3.8 5.1 6.6 6.6l2.2-2.2c.3-.3.7-.4 1-.2 1.1.4 2.3.6 3.6.6.6 0 1 .4 1 1V20c0 .6-.4 1-1 1C10.6 21 3 13.4 3 4c0-.6.4-1 1-1h3.5c.6 0 1 .4 1 1 0 1.3.2 2.5.6 3.6.1.3 0 .7-.2 1z"/>
        </svg>
        +64215550192
      </span>
    </div>
  </section>
</main>
</body>
</html>
```